Car transport business

We need a new business card design. Attached is our old card sample. I would just like to adjust the logo colors (blue and red) to be brighter. I changed my name to the brighter red and the word dispatcher to a brighter blue as an example. But you can adjust those colors further. And then perhaps you can use the same colors for the card design but use your imagination.

As a suggestion so the card stands out I would like to add a clip art of car carrier truck. Attached are examples of that as well

```html
<!DOCTYPE html>
<html lang="en">
<head>
<meta charset="UTF-8">
<title>Crestline Haul — Business Card</title>
<link rel="stylesheet" href="https://fonts.googleapis.com/css2?family=Red+Hat+Display:ital,wght@0,400;0,500;0,600;0,700;1,500&display=swap">
<style>
  :root {
    --card-bg: #ffffff;
    --brand-red: #ff1a0a;
    --brand-blue: #2f7df6;
    --mark-blue: #1c4fa8;
    --art-light: #f2f2f2;
    --art-mid: #e4e4e4;
  }
  html, body {
    margin: 0;
    padding: 0;
    width: 1200px;
    height: 686px;
    overflow: hidden;
    background: var(--card-bg);
  }
  .card {
    position: relative;
    width: 1200px;
    height: 686px;
    background: var(--card-bg);
    font-family: "Red Hat Display", Arial, sans-serif;
    overflow: hidden;
  }
  .truck-art {
    position: absolute;
    left: 207px;
    top: 98px;
    width: 913px;
    height: 505px;
    border-radius: 40px;
    background: radial-gradient(ellipse at 60% 50%, var(--art-mid) 0%, var(--art-light) 55%, rgba(255,255,255,0) 78%);
  }
  .brand {
    position: absolute;
    left: 88px;
    top: 150px;
    display: flex;
    flex-direction: column;
    gap: 8px;
  }
  .brand-row {
    display: flex;
    align-items: center;
    gap: 16px;
  }
  .brand-dot {
    width: 50px;
    height: 50px;
    border-radius: 50%;
    background: var(--brand-red);
  }
  .brand-name {
    font-weight: 700;
    font-size: 46px;
    letter-spacing: 1px;
    color: var(--mark-blue);
    line-height: 1;
  }
  .brand-tagline {
    font-weight: 500;
    font-size: 15.5px;
    letter-spacing: 2.6px;
    color: var(--mark-blue);
    margin-left: 82px;
    white-space: nowrap;
  }
  .person {
    position: absolute;
    left: 86px;
    top: 494px;
  }
  .person-name {
    font-weight: 600;
    font-size: 64px;
    color: var(--brand-red);
    line-height: 1;
    margin: 0;
  }
  .person-role {
    font-weight: 500;
    font-style: italic;
    font-size: 34px;
    letter-spacing: 2.5px;
    color: var(--brand-blue);
    margin: 14px 0 0 2px;
  }
  .contacts {
    position: absolute;
    left: 618px;
    top: 441px;
    list-style: none;
    margin: 0;
    padding: 0;
  }
  .contact-item {
    display: flex;
    align-items: center;
    height: 60px;
    font-size: 36px;
    color: var(--brand-red);
  }
  .contact-icon {
    width: 24px;
    height: 24px;
    margin-right: 40px;
    flex: none;
  }
</style>
</head>
<body>
<div class="card">
  <div class="truck-art" role="img" aria-label="Faint grey clip art of a car carrier truck loaded with vehicles"></div>

  <div class="brand">
    <div class="brand-row">
      <span class="brand-dot"></span>
      <span class="brand-name">CRESTLINE HAUL</span>
    </div>
    <span class="brand-tagline">COAST TO COAST VEHICLE SHIPPING</span>
  </div>

  <div class="person">
    <h1 class="person-name">Omar Vesna</h1>
    <p class="person-role">DISPATCHER</p>
  </div>

  <ul class="contacts">
    <li class="contact-item">
      <svg class="contact-icon" viewBox="0 0 24 24" fill="none" stroke="var(--brand-red)" stroke-width="1.8" stroke-linejoin="round" aria-hidden="true">
        <path d="M5 3h4l2 5-2.5 1.5a11 11 0 0 0 6 6L16 13l5 2v4a2 2 0 0 1-2 2A17 17 0 0 1 3 5a2 2 0 0 1 2-2z"/>
      </svg>
      <span>555-318-2740</span>
    </li>
    <li class="contact-item">
      <svg class="contact-icon" viewBox="0 0 24 24" fill="none" stroke="var(--brand-red)" stroke-width="1.8" stroke-linejoin="round" aria-hidden="true">
        <rect x="3" y="9" width="18" height="12" rx="1.5"/>
        <rect x="7" y="3" width="10" height="6"/>
        <path d="M7 13h2M11 13h2M15 13h2M7 17h2M11 17h2M15 17h2"/>
      </svg>
      <span>555-318-2741</span>
    </li>
    <li class="contact-item">
      <svg class="contact-icon" viewBox="0 0 24 24" fill="none" stroke="var(--brand-red)" stroke-width="1.8" stroke-linejoin="round" aria-hidden="true">
        <rect x="3" y="6" width="18" height="13" rx="1"/>
        <path d="M3 7l9 6 9-6"/>
      </svg>
      <span>crestlinehaul@mailbox.com</span>
    </li>
  </ul>
</div>
</body>
</html>
```